Willow Ember Uniform Label Redesign

To refine our current product label designs into one, simple, modern, crisp, general look that can be adapted to all our all Natural Skin Care and Wellness products. I am inspired by the elegant versatility of products like Corvalis Botanic Beauty or Tidal Beauty label schemes. We no longer want labels that indicate scent or ingredients. We have two primary colors that we want to maintain (#096CA3 and #DEE33F), and are willing to entertain subtle additions of others, other than black. Our labels will be printed on white or clear material. We use mainly Cosmo or Boston Round container shapes, plus flat top, smooth, round jars. Maybe a faded watermark highlight the "natural" or "beautiful" side of our products. we need to convey confidence, while remaining simple. We currently use the Advantage font. Maybe Century Gothic may work. Something similar that is easy on the eyes. Maybe vertical main text? We are willing to entertain a lot of ideas. These designs will offer ideas into our eventual Website (www.willowember.com) redesign.

Target Market(s)

Those who are familiar with the power of natural, plant based skin care and wellness products

Industry/Entity Type

Natural Skin Care and Wellness

Font styles to use
Sans Serif
Other font styles liked:
• Century Gothic, Advantage, or similar that is easy on the eyes

Colors
0054AA
0677BA
7BADD7
CADEEF
E8F1F8
59FF00
82FF00
B8FF75
E3FFCB
F4FFEA

Requirements
Must have
• "Clean Lines"; These colors: (#096CA3 and #DEE33F)
Nice to have
• MAYBE vertical main text or a watermark image

```html
<!DOCTYPE html>
<html lang="en">
<head>
<meta charset="utf-8">
<title>Willow Ember — Label System</title>
<link rel="stylesheet" href="https://fonts.googleapis.com/css2?family=Lexend:wght@300&family=Crimson+Pro:wght@400&display=swap">
<style>
  :root {
    --lime: #dee33f;
    --blue: #096ca3;
    --ink: #1f1f1f;
    --paper: #ffffff;
    --shadow: #d6d6d6;
    --sans: "Lexend", "Century Gothic", sans-serif;
    --serif: "Crimson Pro", Georgia, serif;
  }
  html, body {
    margin: 0;
    width: 1200px;
    height: 1200px;
    overflow: hidden;
    background: var(--paper);
  }
  .sheet {
    position: relative;
    width: 1200px;
    height: 1200px;
    font-family: var(--sans);
    color: var(--ink);
  }
  .label {
    position: absolute;
    background: var(--paper);
    box-shadow: 10px 10px 0 var(--shadow);
  }
  .label--tall { left: 125px; top: 87px; width: 430px; height: 803px; }
  .label--square { left: 581px; top: 481px; width: 420px; height: 409px; }
  .label--wide { left: 124px; top: 947px; width: 790px; height: 209px; }

  .centered {
    position: absolute;
    transform: translate(-50%, -50%);
    white-space: nowrap;
    text-align: center;
    margin: 0;
    line-height: 1;
  }
  .brand-name {
    font-weight: 300;
    text-transform: uppercase;
    letter-spacing: 0.12em;
  }
  .tagline { font-weight: 300; letter-spacing: 0.02em; }
  .product-name { font-weight: 300; text-transform: uppercase; line-height: 1.02; }
  .product-line { font-family: var(--serif); font-weight: 400; color: var(--blue); }
  .volume { font-weight: 300; }
  .brand-dot {
    position: absolute;
    transform: translate(-50%, -50%);
    border-radius: 50%;
    background: var(--lime);
  }
  .accent-bar { position: absolute; background: var(--lime); }
</style>
</head>
<body>
<main class="sheet">

  <section class="label label--tall">
    <p class="centered brand-name" style="left:209px; top:144px; font-size:30px;">Willow Ember</p>
    <p class="centered tagline" style="left:209px; top:175px; font-size:17px;">simple | beautiful | timeless</p>
    <span class="brand-dot" style="left:208px; top:380px; width:300px; height:300px;"></span>
    <h2 class="centered product-name" style="left:208px; top:604px; font-size:26px;">Magnesium<br>Lotion</h2>
    <p class="centered product-line" style="left:208px; top:657px; font-size:23px;">Natural Skin Care</p>
    <span class="accent-bar" style="left:126px; top:679px; width:168px; height:20px;"></span>
    <p class="centered volume" style="left:208px; top:744px; font-size:17px;">120ml</p>
  </section>

  <section class="brand-lockup">
    <span class="brand-dot" style="left:884px; top:187px; width:150px; height:150px;"></span>
    <p class="centered brand-name" style="left:900px; top:320px; font-size:46px;">Willow Ember</p>
    <p class="centered tagline" style="left:900px; top:372px; font-size:26px;">simple | beautiful | timeless</p>
  </section>

  <section class="label label--square">
    <p class="centered brand-name" style="left:205px; top:65px; font-size:23px;">Willow Ember</p>
    <p class="centered tagline" style="left:205px; top:91px; font-size:14px;">simple | beautiful | timeless</p>
    <span class="brand-dot" style="left:122px; top:211px; width:148px; height:148px;"></span>
    <span class="accent-bar" style="left:203px; top:150px; width:133px; height:16px;"></span>
    <h2 class="centered product-name" style="left:270px; top:198px; font-size:20px;">Hydrating<br>Serum</h2>
    <p class="centered product-line" style="left:270px; top:236px; font-size:20px;">Skin Care</p>
    <span class="accent-bar" style="left:203px; top:252px; width:133px; height:16px;"></span>
    <p class="centered volume" style="left:206px; top:358px; font-size:18px;">120ml</p>
  </section>

  <section class="label label--wide">
    <p class="centered brand-name" style="left:392px; top:14px; font-size:23px;">Willow Ember</p>
    <p class="centered tagline" style="left:392px; top:40px; font-size:14px;">simple | beautiful | timeless</p>
    <span class="brand-dot" style="left:312px; top:125px; width:126px; height:126px;"></span>
    <span class="accent-bar" style="left:383px; top:70px; width:120px; height:13px;"></span>
    <h2 class="centered product-name" style="left:443px; top:113px; font-size:15px;">Magnesium<br>Lotion</h2>
    <p class="centered product-line" style="left:443px; top:144px; font-size:14px;">Natural Skin Care</p>
    <span class="accent-bar" style="left:383px; top:162px; width:120px; height:13px;"></span>
    <p class="centered volume" style="left:444px; top:194px; font-size:12px;">120ml</p>
  </section>

</main>
</body>
</html>
```